Consulting and investment firm, logo design is needed as well.

I am looking to open a consulting firm. Where myself is currently an investor, entrepreneur and consultant for many businesses.

The company name is Morvik Company Limited
The logo should communicate prestige like luxury or gold or money, trustworthy and modern.

Overall name card Color can be: white, black, blue, gold, silver (you can choose one, few or all of it, up to you)

It would be great if you can provide raw file like .psd for me so that I can make some little amendment in future and inserting company name or remove it. Because I would also like to use it as only under my name too (some card I will remove the company name).

• I want it to look modern.

```html
<!DOCTYPE html>
<html lang="en">
<head>
<meta charset="UTF-8">
<title>Morvik Company Limited – Business Card</title>
<link rel="stylesheet" href="https://fonts.googleapis.com/css2?family=Lexend:wght@400;500;600&display=swap">
<style>
  :root {
    --brand-blue: #1b4f8e;
    --text-grey: #7b7b7b;
    --band-grey: #8a8a8a;
    --paper: #ffffff;
  }
  * { margin: 0; padding: 0; box-sizing: border-box; }
  html, body { width: 1200px; height: 664px; overflow: hidden; background: var(--paper); }
  .card {
    position: relative;
    width: 1200px;
    height: 664px;
    background: var(--paper);
    font-family: "Lexend", sans-serif;
    overflow: hidden;
  }

  .holder {
    position: absolute;
    right: 42px;
    top: 48px;
    text-align: right;
  }
  .holder-name {
    color: var(--brand-blue);
    font-size: 47px;
    font-weight: 600;
    line-height: 1;
    letter-spacing: 0.2px;
  }
  .holder-title {
    margin-top: 12px;
    color: var(--text-grey);
    font-size: 28px;
    font-weight: 500;
    line-height: 1;
  }

  .brand {
    position: absolute;
    left: 107px;
    top: 228px;
    width: 454px;
    text-align: center;
    color: var(--brand-blue);
    font-weight: 500;
  }
  .brand-square {
    display: block;
    width: 150px;
    height: 150px;
    margin: 0 auto;
    background: var(--brand-blue);
  }
  .brand-name {
    margin-top: 58px;
    font-size: 62px;
    line-height: 1;
    letter-spacing: 30px;
    margin-right: -30px;
  }
  .brand-sub {
    margin-top: 18px;
    font-size: 27px;
    line-height: 1;
    letter-spacing: 9.5px;
    margin-right: -9.5px;
  }

  .contacts {
    position: absolute;
    left: 640px;
    top: 258px;
    list-style: none;
  }
  .contact {
    display: flex;
    align-items: center;
    height: 52px;
    color: var(--text-grey);
    font-size: 31px;
    font-weight: 500;
  }
  .contact + .contact { margin-top: 56px; }
  .contact-icon {
    width: 40px;
    display: flex;
    justify-content: center;
    margin-right: 44px;
    fill: var(--brand-blue);
  }

  .base-bands {
    position: absolute;
    left: 0;
    bottom: 0;
    width: 1200px;
    height: 17px;
  }
  .band-grey { fill: var(--band-grey); }
  .band-blue { fill: var(--brand-blue); }
</style>
</head>
<body>
  <div class="card">
    <header class="holder">
      <div class="holder-name">Owner Name</div>
      <div class="holder-title">Managing Director</div>
    </header>

    <div class="brand">
      <span class="brand-square"></span>
      <div class="brand-name">MORVIK</div>
      <div class="brand-sub">COMPANY LIMITED</div>
    </div>

    <ul class="contacts">
      <li class="contact">
        <span class="contact-icon">
          <svg width="26" height="42" viewBox="0 0 26 42" aria-hidden="true">
            <path d="M4 0h18a4 4 0 0 1 4 4v34a4 4 0 0 1-4 4H4a4 4 0 0 1-4-4V4a4 4 0 0 1 4-4zm-1 6v28h20V6zm10 30a2 2 0 1 0 0.01 0z" fill-rule="evenodd"/>
          </svg>
        </span>
        <span class="contact-text">1234567890</span>
      </li>
      <li class="contact">
        <span class="contact-icon">
          <svg width="32" height="48" viewBox="0 0 32 48" aria-hidden="true">
            <path d="M16 0C7.2 0 0 7 0 15.8 0 27 16 48 16 48s16-21 16-32.2C32 7 24.8 0 16 0zm0 22a6.5 6.5 0 1 1 0-13 6.5 6.5 0 0 1 0 13z" fill-rule="evenodd"/>
          </svg>
        </span>
        <span class="contact-text">Address 1, Address 2</span>
      </li>
      <li class="contact">
        <span class="contact-icon">
          <svg width="38" height="30" viewBox="0 0 38 30" aria-hidden="true">
            <path d="M0 0h38v30H0zm3 3v24h32V3zm1.5 1.5L19 16 33.5 4.5 35 6.5 19 19.5 3 6.5zM3 25l11-10 1.8 1.8L5 26.5zm32 0L24 15l-1.8 1.8L33 26.5z" fill-rule="evenodd"/>
          </svg>
        </span>
        <span class="contact-text">hello@morvikco.com</span>
      </li>
    </ul>

    <svg class="base-bands" viewBox="0 0 1200 17" aria-hidden="true">
      <polygon class="band-grey" points="0,0 233,0 221,17 0,17"/>
      <polygon class="band-blue" points="242,0 1200,0 1200,17 230,17"/>
    </svg>
  </div>
</body>
</html>
```